Health - Quiet Meadow Project

I am running a new Quiet Meadow Conference that will have meditation, mediums and healers - this is a first time conference. However the conference is aimed at mainstream 'normal' people. The 'normal' people, don't want to hear or see words like Tantra, Prana, Angels, etc, but they have problems that can be alleviated through these mediums. The design should communicate light, soothing, comforting, healing. I would like a web design for a single page that can be used as a landing page for the conference registration. I also need a logo and a flyer that can be made into posters A4 or A3 posters. I need to be able to edit all documents as there will be changes in the program through time. I have attached the initial agenda. This conference will be held in Victoria, Australia.
Target Market(s)
Mums and grandmas
Industry/Entity Type
Health And Wellness
Number of Pages Required
1 page
Look and feel
Each slider illustrates characteristics of the customer's brand and the style your logo design should communicate.

```html
<!DOCTYPE html>
<html lang="en">
<head>
<meta charset="utf-8">
<title>Quiet Meadow Conference</title>
<link href="https://fonts.googleapis.com/css2?family=Lato:wght@400;700&family=Great+Vibes&display=swap" rel="stylesheet">
<style>
:root{
  --teal:#33b3a6;
  --teal-dark:#27978c;
  --ink:#4a4a4a;
  --muted:#8a8a8a;
  --line:#e3e3e3;
  --paper:#ffffff;
  --strip:#2a9d92;
}
*{margin:0;padding:0;box-sizing:border-box}
html,body{width:1200px;height:2432px;overflow:hidden;background:var(--paper);font-family:"Lato",sans-serif;color:var(--ink)}
.hero{position:relative;height:524px;background:linear-gradient(100deg,#6b5a49 0%,#a38f78 30%,#cfc4b3 55%,#8c8f86 80%,#5d5f57 100%)}
.hero-brand{position:absolute;left:40px;top:34px;color:#fff;font-size:30px;font-weight:700;display:flex;align-items:center;gap:10px}
.hero-brand .dot{width:14px;height:14px;border-radius:50%;background:var(--teal)}
.hero-title{position:absolute;left:104px;top:362px;font-family:"Great Vibes",cursive;font-size:64px;color:#fff}
.hero-btn{position:absolute;left:104px;top:454px;background:#fff;color:var(--teal-dark);font-size:16px;font-weight:700;padding:9px 20px}
.arrow{position:absolute;top:248px}
.arrow.left{left:26px}.arrow.right{right:26px}
.band{height:72px;background:var(--teal);color:#fff;font-size:40px;font-weight:700;display:flex;align-items:center;justify-content:center;gap:26px}
.speakers{padding:48px 80px 0}
.section-title{font-size:30px;font-weight:700;color:var(--teal-dark);padding-bottom:16px;border-bottom:2px solid var(--teal);margin-bottom:36px;position:relative}
.grid{display:grid;grid-template-columns:1fr 1fr;gap:36px 40px}
.card{border:1px solid var(--line);height:700px;padding:42px 40px;text-align:center;box-shadow:0 2px 6px rgba(0,0,0,.05)}
.card:nth-child(n+3){height:600px}
.portrait{width:150px;height:150px;border-radius:50%;margin:0 auto 26px;border:4px solid #fff;box-shadow:0 0 0 1px var(--line)}
.p1{background:radial-gradient(circle at 50% 45%,#e9b894,#a9553a 70%)}
.p2{background:radial-gradient(circle at 50% 45%,#e5c0a0,#b2b6a4 70%)}
.p3{background:radial-gradient(circle at 50% 45%,#e4c1a4,#8aa6c8 70%)}
.p4{background:radial-gradient(circle at 50% 45%,#c8a889,#6f8a58 70%)}
.name{font-size:30px;color:#333;margin-bottom:6px}
.topic{font-size:16px;font-weight:700;color:#555;margin-bottom:10px}
.time{font-size:15px;color:var(--teal);margin-bottom:22px}
.bio{font-size:14px;line-height:1.9;color:var(--muted);text-align:left}
.more{display:block;margin-top:40px;font-size:14px;color:var(--teal)}
.footer{position:absolute;left:0;top:2180px;width:1200px;height:252px;background:var(--teal);color:#fff}
.footer-brand{position:absolute;left:80px;top:80px;font-size:34px;font-weight:700;display:flex;align-items:center;gap:10px}
.footer-brand .dot{width:14px;height:14px;border-radius:50%;background:#fff}
.contact{position:absolute;left:500px;top:40px}
.contact h3{font-size:22px;font-weight:400;margin-bottom:20px}
.contact p{display:flex;align-items:center;gap:12px;font-size:14px;margin-bottom:14px}
.map{position:absolute;right:80px;top:30px;width:300px;height:130px;background:linear-gradient(135deg,#eef0ea,#d8ddd2)}
.map span{position:absolute;left:14px;top:14px;background:#fff;color:#444;font-size:12px;line-height:1.4;padding:6px 8px;box-shadow:0 1px 3px rgba(0,0,0,.2)}
.strip{position:absolute;left:0;bottom:0;width:100%;height:70px;background:var(--strip);display:flex;align-items:center;justify-content:center;font-size:13px}
.strip .page{position:absolute;right:80px}
</style>
</head>
<body>
<header class="hero" role="img" aria-label="Photo of a pale butterfly resting on a hanging bell with a soft blurred background">
  <div class="hero-brand"><span class="dot"></span>Quiet Meadow</div>
  <svg class="arrow left" width="20" height="36" viewBox="0 0 20 36"><path d="M17 3 3 18l14 15" fill="none" stroke="#fff" stroke-width="3"/></svg>
  <svg class="arrow right" width="20" height="36" viewBox="0 0 20 36"><path d="M3 3l14 15L3 33" fill="none" stroke="#fff" stroke-width="3"/></svg>
  <div class="hero-title">Listen to the Bell of Change</div>
  <div class="hero-btn">Conference Registration</div>
</header>

<div class="band"><span>Quiet Meadow Conference</span><span>Saturday August 20th 2016</span></div>

<main class="speakers">
  <h2 class="section-title">Our Speakers</h2>
  <div class="grid">
    <article class="card">
      <div class="portrait p1" role="img" aria-label="Portrait photo of speaker Laurel Devane"></div>
      <h3 class="name">Laurel Devane</h3>
      <p class="topic">Embodying Upon the Spiritual Life</p>
      <p class="time">9:00 - 10:00</p>
      <p class="bio">A modern day spiritual facilitator, Laurel is a teacher and guide whose approach to wellbeing is practical and warm. She helps people reconnect with calm, clarity and purpose, blending gentle meditation with everyday tools that support lasting change in family life, work and health. Her sessions leave guests feeling lighter and heard.</p>
      <a class="more">Read More &gt;&gt;</a>
    </article>
    <article class="card">
      <div class="portrait p2" role="img" aria-label="Portrait photo of speaker Lila Marsh"></div>
      <h3 class="name">Lila Marsh</h3>
      <p class="topic">Conscious Connection &amp; Living Life Fully</p>
      <p class="time">11:00 - 12:00</p>
      <p class="bio">With a background in coaching, psychology and holistic care, Lila has spent many years helping women find balance and confidence. Her talks are full of humour and honesty, offering simple practices for rest, connection and joy that anyone can bring home and use every single day with ease.</p>
      <a class="more">Read More &gt;&gt;</a>
    </article>
    <article class="card">
      <div class="portrait p3" role="img" aria-label="Portrait photo of speaker Paul Fenton"></div>
      <h3 class="name">Paul Fenton</h3>
      <p class="topic">The Slow Breath to Freedom</p>
      <p class="time">1:00 - 2:00</p>
      <p class="bio">Paul has over thirty years of experience in breathing and relaxation practice. He shows how slowing the breath can ease stress, improve sleep and restore energy, with clear steps that suit busy parents and grandparents alike.</p>
      <a class="more">Read More &gt;&gt;</a>
    </article>
    <article class="card">
      <div class="portrait p4" role="img" aria-label="Portrait photo of speaker Willow Hart"></div>
      <h3 class="name">Willow Hart</h3>
      <p class="topic">Sound &amp; Stillness</p>
      <p class="time">3:00 - 4:00</p>
      <p class="bio">A loving soul, devoted wife and mother, Willow brings soothing sound sessions that invite deep rest. Her gentle, grounded style helps guests let go of tension and leave the day feeling refreshed, supported and calm.</p>
      <a class="more">Read More &gt;&gt;</a>
    </article>
  </div>
</main>

<footer class="footer">
  <div class="footer-brand"><span class="dot"></span>Quiet Meadow</div>
  <div class="contact">
    <h3>Contact Us</h3>
    <p><svg width="16" height="16" viewBox="0 0 16 16"><path d="M3 1h3l1 4-2 1a9 9 0 0 0 5 5l1-2 4 1v3a2 2 0 0 1-2 2A13 13 0 0 1 1 3a2 2 0 0 1 2-2z" fill="#fff"/></svg>Call us: 0400 123 456</p>
    <p><svg width="16" height="16" viewBox="0 0 16 16"><rect x="1" y="3" width="14" height="10" fill="none" stroke="#fff" stroke-width="1.5"/><path d="M1 3l7 6 7-6" fill="none" stroke="#fff" stroke-width="1.5"/></svg>hello@quietmeadowproject.example</p>
  </div>
  <div class="map" role="img" aria-label="Street map showing the conference venue"><span>12 Linden Way, Fernvale<br>VIC 3999</span></div>
  <div class="strip">© Quiet Meadow Project 2016 · All Rights Reserved · Privacy Policy<span class="page">1 / 6</span></div>
</footer>
</body>
</html>
```